Business card design needed

the business is HR Consulting, but its for SME businesses who cant afford a permanent HR person. We sell an HR info system to help them meet minimum employment legislation but with this hope they then require us on a monthly subscription to phone or email us for HR advice. We are HR qualified mums working from home

So we will be partners to HR and Payroll systems known as kindle HR and Pluto

Target Market(s)

Small to medium businesses so not black and overly corporate, but having said that many are accounting businesses

Industry/Entity Type

Business

Contact Information for Business Card

Name of the company: Sorrelby Advisory

Me:Marta Kovalenko
Title:Managing Director

m: 0437 215 683
e: marta@sorrelby.com.au
w: www.sorrelby.com.au

What we do: HR Consulting, HR Systems and support, Payroll Advice

Requirements
Nice to have
• there is a company already out there known as Quartz professionals. I like the leaves at the end as I wanted something different like this to the usual business logos but still professional. I wanted a symbol to show calm, positive, ease flow going up ,etc. but realise they have the leaves and possibly cant copy, or can we?..( kite??, something calm and positive)dont know!!. Green and blue needed to be in it as nature and calm as well. I love the colours of www.stafflanefund.com ( attached the colours), as well as the calm wave line underneath. have a look as while they use green and blue I loved the purple colour thrown in there.Green and blue on their own are so overused. I want vibrant. I want double sided and when on a table I want it to stand out so maybe the purple colour (as per the colours on the fund website) solid on one side with just the 3 services we provide and personal and company name on front but need some creativity from you guys.

```html
<!DOCTYPE html>
<html lang="en">
<head>
<meta charset="utf-8">
<title>Sorrelby Advisory – Business Card</title>
<link rel="stylesheet" href="https://fonts.googleapis.com/css2?family=Questrial&display=swap">
<style>
  :root {
    --teal: #45b2bd;
    --purple: #a8479a;
    --magenta: #b23b97;
    --paper: #f2f2f3;
    --white: #ffffff;
    --stage: #2b2b2d;
  }
  * { box-sizing: border-box; margin: 0; padding: 0; }
  html, body {
    width: 1200px; height: 900px; overflow: hidden;
    background: var(--stage);
    font-family: "Questrial", "Century Gothic", sans-serif;
  }
  .canvas { position: relative; width: 1200px; height: 900px; }

  .card {
    position: absolute;
    width: 620px; height: 378px;
    overflow: hidden;
  }

  /* Back side */
  .card-back {
    left: 110px; top: 50px;
    background: var(--teal);
    color: var(--white);
  }
  .card-back .brand-name {
    position: absolute; left: 70px; top: 128px;
    font-size: 52px; line-height: 1; color: var(--white);
    white-space: nowrap;
  }
  .services {
    position: absolute; left: 84px; top: 212px;
    list-style: none; font-size: 21px; line-height: 1.45;
  }
  .services li span::before { content: "\2022"; margin-right: 4px; }
  .services li span + span { margin-left: 12px; }

  /* Front side */
  .card-front {
    left: 470px; top: 472px;
    background: var(--paper);
  }
  .card-front .wave { position: absolute; inset: 0; width: 100%; height: 100%; }
  .card-front .brand-name {
    position: absolute; left: 48px; top: 82px;
    font-size: 44px; line-height: 1; color: var(--purple);
    white-space: nowrap;
  }
  .contact {
    position: absolute; right: 34px; top: 168px;
    text-align: right; color: var(--white);
  }
  .contact .person { font-size: 24px; color: var(--magenta); }
  .contact .role { font-size: 15px; margin-top: 4px; }
  .contact .lines { font-size: 16px; margin-top: 20px; line-height: 1.35; }
  .contact .label { color: var(--magenta); }
  .contact .web { color: var(--magenta); }
</style>
</head>
<body>
<main class="canvas">

  <section class="card card-back" aria-label="Business card, back">
    <p class="brand-name">Sorrelby Advisory</p>
    <ul class="services">
      <li><span>HR Consulting</span><span>HR Strategy</span></li>
      <li><span>HR Systems and Support</span></li>
    </ul>
  </section>

  <section class="card card-front" aria-label="Business card, front">
    <svg class="wave" viewBox="0 0 620 378" preserveAspectRatio="none" aria-hidden="true">
      <path d="M0,318 C160,290 280,190 410,150 C490,126 560,118 620,116 L620,378 L0,378 Z" fill="var(--teal)"/>
      <path d="M0,300 C160,272 280,172 410,132 C490,108 560,100 620,98" fill="none" stroke="var(--purple)" stroke-width="9"/>
    </svg>

    <p class="brand-name">Sorrelby Advisory</p>

    <div class="contact">
      <p class="person">Marta Kovalenko</p>
      <p class="role">Managing Director</p>
      <div class="lines">
        <p><span class="label">m:</span> 0437 215 683 &nbsp;<span class="label">e:</span> marta@sorrelby.com.au</p>
        <p class="web">www.sorrelby.com.au</p>
      </div>
    </div>
  </section>

</main>
</body>
</html>
```